Looking for a label design for a product call KAVA. My business is to sell prepack kava to stores and online.
I need Hawaiian Polynesian theme around tradition.

The label need to have "Nalu Kava" that's the name of the product. Can add "traditional herbal drink"

Can be colorful, the label will be print in a oval shape clear label size 4.25"x3.25" and will be put on a black back ground.

I don't want any white.

Target Market(s)

Polynesian population and tourist

Industry/Entity Type

Business

Requirements
Must have
• Name: Nalu Kava
inscription: Traditional Herbal drink
inscription: 100% Dried Powder Kava Roots
Net Wt: 8oz
Nice to have
• Traditional art design.

```html
<!DOCTYPE html>
<html lang="en">
<head>
<meta charset="utf-8">
<title>Nalu Kava – Label</title>
<link rel="stylesheet" href="https://fonts.googleapis.com/css2?family=Pinyon+Script&family=Alegreya:wght@700&display=swap">
<style>
  :root {
    --backdrop: #e4e4e4;
    --sky-dark: #1a0e08;
    --sky-deep: #5a2a12;
    --sky-ember: #b5551f;
    --sky-glow: #d98a4a;
    --horizon: #efd9a8;
    --leaf-dark: #3f5a3a;
    --leaf-mid: #7f9b78;
    --label-text: #ffffff;
  }
  html, body {
    margin: 0;
    padding: 0;
    width: 1200px;
    height: 1000px;
    overflow: hidden;
    background: var(--backdrop);
  }
  .canvas {
    position: relative;
    width: 1200px;
    height: 1000px;
  }
  .label-art {
    position: absolute;
    left: 0;
    top: 0;
  }
  .label-text {
    position: absolute;
    left: 0;
    width: 1200px;
    text-align: center;
    color: var(--label-text);
    margin: 0;
    line-height: 1;
    white-space: nowrap;
  }
  .brand-first {
    font-family: "Pinyon Script", cursive;
    font-weight: 400;
    font-size: 170px;
    top: 150px;
    padding-left: 240px;
    box-sizing: border-box;
  }
  .brand-second {
    font-family: "Pinyon Script", cursive;
    font-weight: 400;
    font-size: 330px;
    top: 215px;
  }
  .tagline {
    font-family: "Pinyon Script", cursive;
    font-size: 66px;
    top: 548px;
    text-shadow: 3px 4px 4px rgba(0,0,0,0.8);
  }
  .contents {
    font-family: "Alegreya", serif;
    font-weight: 700;
    font-size: 38px;
    top: 686px;
    padding-left: 14px;
    box-sizing: border-box;
    text-shadow: 2px 2px 3px rgba(0,0,0,0.85);
  }
  .net-weight {
    font-family: "Alegreya", serif;
    font-weight: 700;
    font-size: 40px;
    top: 734px;
    text-shadow: 2px 2px 3px rgba(0,0,0,0.85);
  }
</style>
</head>
<body>
<div class="canvas">
  <svg class="label-art" width="1200" height="1000" viewBox="0 0 1200 1000">
    <defs>
      <linearGradient id="sunsetScene" x1="0" y1="0" x2="0" y2="1">
        <stop offset="0" stop-color="var(--sky-dark)"/>
        <stop offset="0.12" stop-color="var(--sky-deep)"/>
        <stop offset="0.4" stop-color="var(--sky-ember)"/>
        <stop offset="0.62" stop-color="var(--sky-glow)"/>
        <stop offset="0.74" stop-color="var(--horizon)"/>
        <stop offset="0.8" stop-color="var(--leaf-mid)"/>
        <stop offset="1" stop-color="var(--leaf-dark)"/>
      </linearGradient>
    </defs>
    <ellipse class="label-shape" cx="607" cy="476" rx="482" ry="370"
             fill="url(#sunsetScene)" role="img"
             aria-label="Photograph of a hula dancer silhouetted against a fiery Hawaiian sunset sky above green kava leaves"/>
  </svg>

  <p class="label-text brand-first">Nalu</p>
  <p class="label-text brand-second">Kava</p>
  <p class="label-text tagline">Traditional Herbal Drink</p>
  <p class="label-text contents">100% Dried Powder Kava Roots</p>
  <p class="label-text net-weight">Net Wt: 8oz</p>
</div>
</body>
</html>
```